Delivery Docket urgent plus require many other designs for more stationary after this.

We need a new delivery docket design urgently as the one we have needs updating and we have changed our company name. Please do not copy the one I have uploaded as we do not feel this looks professional enough. I uploaded it as a few designers requested to see what we are currently using thank you.
It is quite complex in that we need a range of information to be on the one docket.
We are a Transport Company based in Australia that has a wide variety of items that we deliver such as water, sand and gravels and heavy equipment transport.
We would prefer to keep this design to A5 size as we will get them made into books. We are looking for a modern professional look. Although it is only a delivery docket this is given to all our customers so needs to look impressive.

We need our new logo on the docket (PVR). There will also need to be areas for our address and contact numbers, email etc these will be supplied to the winning designer to make the final adjustments so for now just put something generic in these spaces.
Needs to have an area for customer details, purchase order number, date and docket number (docket number to be in red)
Needs a section where we can list the type of product / and or service that has been provided and the amount / qty usually 3 lines will be enough for this. Need area under this where the customer can sign name and print name to say that the goods / and or services have been received.

Also required somewhere on the docket are the words, Tax Invoice will be issued based on the information provided on this docket. Conditions on back of page

We then need a separate section on the same page which we will use internally that the staff member can tear off and hand into the office. On this section it needs to have area where the driver can list km at start of job and at end with space to calculate km travelled, details of fuel purchased eg amount and litres, vehicle that is being used. also need to log down wheel bearing temps.
prime mover needs spaces as follows
Steer axel FL____________ Steer axel FR _________ 1st drive axel L_______
1st drive axel R_________ 2nd drive axel L_______ 2nd drive axel R________

For the trailers need something similar x 2 as have 2 trailers
1st axel DS_________ 1st axel PS_________ 2nd axel DS__________
2nd axel PS_________ 3rd axel DS_________ 3rd axel PS__________

I have included a few examples of designs we have used in past and ones that we like so you can get an idea of the colours we prefer, I have included some of the designs we are currently receiving for our logo that I like so you can get idea again of colours we prefer. There is much more we need designed also such as time sheets, more delivery dockets and letter heads so there is a lot of more work available to the winning designer.

Thank you

Target Market(s)

Customers

Font styles to use
Serif
Sans Serif

Colors

Designer to choose colors to be used in the design.

Requirements
Should not have
• Please don't copy old docket as we do not like it and nned new info on new design thank you

```html
<!DOCTYPE html>
<html lang="en">
<head>
<meta charset="utf-8">
<title>Delivery Docket</title>
<link rel="stylesheet" href="https://fonts.googleapis.com/css2?family=Archivo:wght@400;600;700&display=swap">
<style>
  :root {
    --ink: #1d1d1d;
    --text: #2b2b2b;
    --band: #d3d4d6;
    --accent: #e8321e;
    --paper: #ffffff;
    --canvas: #efefef;
  }
  * { margin: 0; padding: 0; box-sizing: border-box; }
  html, body { width: 1200px; height: 1200px; overflow: hidden; }
  body {
    background: var(--canvas);
    font-family: "Archivo", Arial, sans-serif;
    color: var(--text);
    position: relative;
  }
  .docket {
    position: absolute;
    left: 40px; top: 209px;
    width: 1120px; height: 782px;
    background: var(--paper);
    overflow: hidden;
  }
  .docket > * { position: absolute; }
  .brand-bar { left: 0; top: 42px; width: 22px; height: 234px; background: var(--band); }
  .brand-name {
    left: 52px; top: 58px;
    display: flex; align-items: center; gap: 14px;
    font-size: 64px; font-weight: 700; letter-spacing: 1px;
    color: var(--ink); line-height: 1;
  }
  .brand-square { width: 18px; height: 18px; background: var(--accent); }
  .contact { left: 52px; top: 144px; font-size: 16px; line-height: 1.3; letter-spacing: -0.3px; }
  .contact-row { display: flex; align-items: flex-start; gap: 6px; margin-bottom: 1px; }
  .contact-row svg { flex: none; margin-top: 2px; }
  .contact-row.indent { padding-left: 20px; }

  .order-bar { left: 644px; top: 55px; width: 18px; height: 73px; background: var(--band); }
  .order { left: 676px; top: 53px; font-size: 18px; line-height: 1.3; letter-spacing: -0.4px; }
  .order b { font-weight: 700; color: var(--ink); margin-right: 6px; }
  .order .po-value { font-size: 21px; }
  .order .docket-no { color: var(--accent); font-size: 22px; }

  .customer {
    left: 644px; top: 144px;
    display: grid; grid-template-columns: 109px auto;
    font-size: 18px; line-height: 1.28; letter-spacing: -0.4px;
  }
  .customer dt { font-weight: 700; color: var(--ink); }
  .customer .phone-value, .customer .phone-label { margin-top: 8px; }

  .items-head {
    left: 55px; top: 278px; width: 1010px; height: 42px;
    background: var(--band);
    font-size: 17px; font-weight: 600; color: #333; letter-spacing: -0.3px;
  }
  .items-head span { position: absolute; top: 11px; }
  .item-line { left: 55px; width: 1010px; height: 2px; background: #333; }

  .sign-line { left: 52px; width: 342px; height: 1px; background: #444; }
  .sign-label { left: 52px; font-size: 12px; letter-spacing: -0.2px; color: #555; }
  .sign-note { left: 52px; top: 640px; font-size: 13px; line-height: 1.36; letter-spacing: -0.3px; }
  .declaration { left: 52px; top: 706px; font-size: 12.5px; line-height: 1.15; letter-spacing: -0.35px; color: var(--ink); }
  .declaration strong { display: block; font-weight: 700; }

  .office-band { left: 0; top: 0; width: 1120px; height: 782px; }
  .driver-title { left: 470px; top: 574px; font-size: 14.5px; letter-spacing: -0.3px; }

  .office-fields { left: 470px; top: 604px; width: 630px; }
  .field-row { display: flex; align-items: flex-end; gap: 14px; height: 19px; }
  .field-row.spaced { margin-bottom: 4px; }
  .row-label { width: 74px; flex: none; font-size: 12px; font-weight: 700; color: var(--ink); white-space: nowrap; }
  .field {
    flex: 1; display: flex; align-items: flex-end;
    font-size: 13px; letter-spacing: -0.35px; white-space: nowrap; color: #333;
  }
  .field i { flex: 1; border-bottom: 1px solid #333; margin-left: 4px; margin-bottom: 3px; }
</style>
</head>
<body>
  <main class="docket">
    <svg class="office-band" viewBox="0 0 1120 782" aria-hidden="true">
      <polygon points="0,746 400,746 445,596 1120,596 1120,782 0,782" fill="var(--band)"/>
    </svg>

    <div class="brand-bar"></div>
    <div class="brand-name"><span>KTD</span><span class="brand-square"></span></div>

    <div class="contact">
      <div class="contact-row">
        <svg width="14" height="18" viewBox="0 0 14 18"><path d="M7 1a6 6 0 0 0-6 6c0 4.5 6 10 6 10s6-5.5 6-10a6 6 0 0 0-6-6zm0 8.5A2.5 2.5 0 1 1 7 4.5a2.5 2.5 0 0 1 0 5z" fill="var(--accent)"/></svg>
        <span>Company address 1, Company Address 2</span>
      </div>
      <div class="contact-row indent"><span>Zip Code 00000 New South Wales</span></div>
      <div class="contact-row">
        <svg width="14" height="16" viewBox="0 0 14 16"><path d="M3 1l3 3-1.5 2c.8 2 2.2 3.6 4 4.5L10.5 9l3 3-2 2.5C6 14 1 8.5 1 3z" fill="var(--accent)"/></svg>
        <span>03 0000 0000</span>
      </div>
      <div class="contact-row">
        <svg width="14" height="16" viewBox="0 0 14 16"><rect x="0.5" y="4" width="13" height="9" fill="var(--accent)"/><path d="M0.5 4l6.5 5 6.5-5" stroke="#fff" stroke-width="1.2" fill="none"/></svg>
        <span>info@KTD.com.au</span>
      </div>
    </div>

    <div class="order-bar"></div>
    <div class="order">
      <div><b>Purchase Order Number:</b><span class="po-value">0019234</span></div>
      <div><b>Date:</b>04/08/2018</div>
      <div><b>Delivery Docket:</b><span class="docket-no">0059</span></div>
    </div>

    <dl class="customer">
      <dt>Customer:</dt>
      <dd>ABC PTE LTD<br>Address 1, Address 2 Address 3<br>Address 4 Zip Code 00000 State</dd>
      <dt class="phone-label">Phone:</dt>
      <dd class="phone-value">03 4567 0000</dd>
    </dl>

    <div class="items-head">
      <span style="left:34px">QUANTITY</span>
      <span style="left:356px">PRODUCT NAME</span>
      <span style="left:713px">DESCRIPTION</span>
    </div>
    <div class="item-line" style="top:366px"></div>
    <div class="item-line" style="top:419px"></div>
    <div class="item-line" style="top:472px"></div>
    <div class="item-line" style="top:524px"></div>

    <div class="sign-line" style="top:566px"></div>
    <div class="sign-label" style="top:570px">Signature</div>
    <div class="sign-line" style="top:612px"></div>
    <div class="sign-label" style="top:616px">Print Name</div>
    <p class="sign-note">Signature Indicates<br>Acceptance and Acknowledgement<br>of Goods/Services received.</p>
    <p class="declaration"><strong>Declaration:</strong>Tax Invoice will be issued based on the information provided<br>on this docket. Conditions on back of page.</p>

    <div class="driver-title">Driver Notes:</div>

    <div class="office-fields">
      <div class="field-row">
        <span class="field">Start Of Job (KM):<i></i></span>
        <span class="field">End of Job (KM):<i></i></span>
        <span class="field">KM Travelled:<i></i></span>
      </div>
      <div class="field-row spaced">
        <span class="field">Type of Vehicle Used:<i></i></span>
        <span class="field">Fuel Purchased (litres):<i></i></span>
      </div>

      <div class="field-row">
        <span class="row-label">Prime Mover</span>
        <span class="field">Steer axel FL:<i></i></span>
        <span class="field">Steer axel FR:<i></i></span>
        <span class="field">1st drive axel L:<i></i></span>
      </div>
      <div class="field-row spaced">
        <span class="row-label"></span>
        <span class="field">1st drive axel R:<i></i></span>
        <span class="field">2nd drive axel L:<i></i></span>
        <span class="field">2nd drive axel R:<i></i></span>
      </div>

      <div class="field-row">
        <span class="row-label">Trailer 1</span>
        <span class="field">1st axel DS:<i></i></span>
        <span class="field">1st axel PS:<i></i></span>
        <span class="field">2nd axel DS:<i></i></span>
      </div>
      <div class="field-row spaced">
        <span class="row-label"></span>
        <span class="field">2nd axel PS:<i></i></span>
        <span class="field">3rd axel DS:<i></i></span>
        <span class="field">3rd axel PS:<i></i></span>
      </div>

      <div class="field-row">
        <span class="row-label">Trailer 2</span>
        <span class="field">1st axel DS:<i></i></span>
        <span class="field">1st axel PS:<i></i></span>
        <span class="field">2nd axel DS:<i></i></span>
      </div>
      <div class="field-row">
        <span class="row-label"></span>
        <span class="field">2nd axel PS:<i></i></span>
        <span class="field">3rd axel DS:<i></i></span>
        <span class="field">3rd axel PS:<i></i></span>
      </div>
    </div>
  </main>
</body>
</html>
```